Business Card Design Project 4 Construction Business

I am after a creative, but sleek and simple/ clean business card design. This design will form the basis of future items and might include a logo or simply a creative way to lay out the text of my company name 'kestrel ventures'
I like the simplicity of black and white however I would also be happy to see a splash of colour introduced somehow to give the text some interest and make it stand out.
I would like a double sided card.
I am young (ish!) and professional, offering construction and project management services, what I don't want is the traditional builders type card featuring a cheesy hammer/ saw image etc.
As the company name, kestrel ventures, suggests, we focus on working closely and collaboratively together, in synergy with all stakeholders involved in the projects that we undertake
Construction

```html
<!DOCTYPE html>
<html lang="en">
<head>
<meta charset="UTF-8">
<title>Kestrel Ventures – Business Card</title>
<link rel="stylesheet" href="https://fonts.googleapis.com/css2?family=Montserrat:wght@400;600;700&display=swap">
<style>
  :root {
    --page-bg: #ececec;
    --card-white: #ffffff;
    --band-dark: #333333;
    --ink-dark: #2e2e2e;
    --ink-light: #f2f2f2;
    --ink-muted: #c9c9c9;
    --rule: #8a8a8a;
  }
  * { margin: 0; padding: 0; box-sizing: border-box; }
  html, body {
    width: 1200px; height: 1000px; overflow: hidden;
    background: var(--page-bg);
    font-family: "Montserrat", sans-serif;
  }
  .sheet {
    width: 1200px; height: 1000px;
    display: flex; flex-direction: column;
    align-items: center; justify-content: center; gap: 40px;
  }
  .card {
    width: 760px; height: 434px;
    background: var(--card-white);
    box-shadow: 0 6px 20px rgba(0,0,0,0.12);
    position: relative; overflow: hidden;
  }
  .wordmark {
    font-weight: 700; color: var(--ink-dark);
    text-transform: uppercase; letter-spacing: 3px;
    white-space: nowrap;
  }
  /* front side */
  .card-front .top-strip {
    height: 120px;
    display: flex; align-items: center; justify-content: flex-end;
    padding-right: 60px;
  }
  .card-front .top-strip .wordmark { font-size: 40px; }
  .card-front .info-band {
    position: absolute; left: 0; right: 0; top: 120px; bottom: 0;
    background: var(--band-dark);
    display: flex; padding: 44px 50px 40px 50px;
  }
  .person {
    width: 300px; text-align: right; padding-right: 34px;
    border-right: 1px solid var(--rule);
    align-self: flex-start; padding-bottom: 60px;
  }
  .person-name { color: var(--ink-light); font-weight: 700; font-size: 26px; }
  .person-role { color: var(--ink-muted); font-style: italic; font-size: 16px; margin-top: 6px; }
  .contact-list { list-style: none; padding-left: 30px; padding-top: 6px; }
  .contact-list li {
    display: flex; align-items: flex-start; gap: 12px;
    color: var(--ink-muted); font-size: 15px; line-height: 1.55;
    margin-bottom: 6px;
  }
  .contact-list svg { width: 15px; height: 15px; flex: none; margin-top: 4px; fill: var(--ink-muted); }
  .contact-list .web { color: var(--ink-light); font-weight: 700; }
  /* back side */
  .card-back {
    display: flex; flex-direction: column;
    align-items: center; justify-content: center; gap: 20px;
  }
  .card-back .wordmark { font-size: 48px; }
  .card-back .site-url { font-weight: 700; font-size: 16px; color: var(--ink-dark); }
</style>
</head>
<body>
<main class="sheet">
  <section class="card card-front" aria-label="Card front">
    <div class="top-strip"><span class="wordmark">Kestrel Ventures</span></div>
    <div class="info-band">
      <div class="person">
        <p class="person-name">Owen Hartley</p>
        <p class="person-role">Director</p>
      </div>
      <ul class="contact-list">
        <li>
          <svg viewBox="0 0 16 16" aria-hidden="true"><path d="M8 1 1 7.5h2V15h4v-4h2v4h4V7.5h2z"/></svg>
          <span>14 Corella St<br>Lindfield NSW 2070</span>
        </li>
        <li>
          <svg viewBox="0 0 16 16" aria-hidden="true"><path d="M4 1 6.5 5 5 6.5c1 2 2.5 3.5 4.5 4.5L11 9.5l4 2.5-1.5 3C7 14.5 1.5 9 1 2.5z"/></svg>
          <span>0412 555 019</span>
        </li>
        <li>
          <svg viewBox="0 0 16 16" aria-hidden="true"><path d="M1 3h14v10H1zm1.5 1.2L8 8.5l5.5-4.3z"/></svg>
          <span>owen@kestrelventuresgroup.com.au</span>
        </li>
        <li>
          <svg viewBox="0 0 16 16" aria-hidden="true"><path d="M8 1a7 7 0 1 0 0 14A7 7 0 0 0 8 1zm0 1.5c.8 0 1.8 1.8 2 4.5H6c.2-2.7 1.2-4.5 2-4.5zM2.6 7h2c.1-1.6.4-3 .9-3.9A5.6 5.6 0 0 0 2.6 7zm8.8 0h2a5.6 5.6 0 0 0-2.9-3.9c.5.9.8 2.3.9 3.9zM2.6 9a5.6 5.6 0 0 0 2.9 3.9c-.5-.9-.8-2.3-.9-3.9zm3.4 0c.2 2.7 1.2 4.5 2 4.5s1.8-1.8 2-4.5zm5.4 0c-.1 1.6-.4 3-.9 3.9A5.6 5.6 0 0 0 13.4 9z"/></svg>
          <span class="web">www.kestrelventuresgroup.com.au</span>
        </li>
      </ul>
    </div>
  </section>

  <section class="card card-back" aria-label="Card back">
    <span class="wordmark">Kestrel Ventures</span>
    <span class="site-url">www.kestrelventuresgroup.com.au</span>
  </section>
</main>
</body>
</html>
```